Business card design

I need my logo on this card, things I need the card to have on it
licensed and insured.
owner operators Derek & Milton Halvorsen
my phone number 5418237906
Disaster Recovery, Storm Damage Restoration, Proactive Disaster Plan Management, Roof Repair/Restoration Structural Repair and Reconstruction, Emergency Boarding and Tarping Service, Perimeter Fencing, Emergency Tree Removal,

```html
<!DOCTYPE html>
<html lang="en">
<head>
<meta charset="utf-8">
<title>Halvorsen's Construction L.L.C – Business Card</title>
<link rel="stylesheet" href="https://fonts.googleapis.com/css2?family=Montserrat:wght@400;500;600&display=swap">
<style>
  :root {
    --backdrop: #979797;
    --card-dark: #141414;
    --card-dark-edge: #1f1f1f;
    --card-light: #f4f4f4;
    --brand-blue: #1b8fe4;
    --text-grey: #5e5e5e;
    --muted-grey: #8a8a8a;
    --white: #ffffff;
  }
  * { margin: 0; padding: 0; box-sizing: border-box; }
  html, body {
    width: 1200px;
    height: 1200px;
    overflow: hidden;
    background: var(--backdrop);
    font-family: "Montserrat", sans-serif;
  }
  .card {
    position: absolute;
    top: 300px;
    width: 437px;
    height: 746px;
    border-radius: 26px;
    overflow: hidden;
    text-align: center;
  }
  /* Front */
  .card-front {
    left: 155px;
    background: var(--card-dark);
  }
  .pattern-field {
    position: absolute;
    inset: 0;
    background: linear-gradient(180deg, var(--card-dark-edge) 0%, var(--card-dark) 55%, #0c0c0c 100%);
  }
  .front-brand {
    position: absolute;
    left: 0;
    right: 0;
    top: 805px;
    top: 505px;
  }
  .brand-mark {
    width: 44px;
    height: 44px;
    margin: 0 auto 24px;
    background: var(--brand-blue);
  }
  .brand-name {
    font-weight: 500;
    text-transform: uppercase;
    line-height: 1.15;
  }
  .brand-name .line-main { display: block; font-size: 38px; letter-spacing: 0.5px; }
  .brand-name .line-sub { display: block; font-size: 14px; letter-spacing: 7px; margin-top: 6px; }
  .front-brand .brand-name { color: var(--white); }
  .licensed-line {
    margin-top: 12px;
    font-size: 11px;
    letter-spacing: 4px;
    color: var(--muted-grey);
    font-weight: 500;
  }
  /* Back */
  .card-back {
    left: 632px;
    background: var(--card-light);
  }
  .back-brand {
    position: absolute;
    left: 0;
    right: 0;
    top: 100px;
  }
  .back-brand .brand-mark { width: 50px; height: 50px; margin-bottom: 40px; }
  .back-brand .brand-name { color: var(--brand-blue); }
  .back-brand .brand-name .line-main { font-size: 44px; }
  .service-list {
    position: absolute;
    left: 0;
    right: 0;
    top: 304px;
    list-style: none;
    font-size: 17.5px;
    line-height: 26.25px;
    color: var(--text-grey);
  }
  .service-list li::before,
  .service-list li::after {
    content: "•";
    color: var(--brand-blue);
    margin: 0 5px;
  }
  .owners {
    position: absolute;
    left: 0;
    right: 0;
    top: 558px;
  }
  .owner-names {
    font-size: 21px;
    font-weight: 600;
    color: var(--brand-blue);
  }
  .owner-role {
    margin-top: 2px;
    font-size: 13px;
    letter-spacing: 1.5px;
    color: var(--text-grey);
    font-weight: 500;
  }
  .phone-divider {
    display: flex;
    align-items: center;
    justify-content: center;
    gap: 8px;
    margin-top: 20px;
  }
  .phone-divider .rule {
    width: 62px;
    height: 2px;
    background: var(--brand-blue);
  }
  .phone-number {
    margin-top: 12px;
    font-size: 20px;
    color: var(--text-grey);
    letter-spacing: 0.5px;
  }
</style>
</head>
<body>
  <section class="card card-front">
    <div class="pattern-field" role="img" aria-label="Repeating embossed monogram pattern in dark tones"></div>
    <div class="front-brand">
      <div class="brand-mark"></div>
      <p class="brand-name">
        <span class="line-main">Halvorsen's</span>
        <span class="line-sub">Construction L.L.C</span>
      </p>
      <p class="licensed-line">• LICENSED &amp; INSURED •</p>
    </div>
  </section>

  <section class="card card-back">
    <div class="back-brand">
      <div class="brand-mark"></div>
      <p class="brand-name">
        <span class="line-main">Halvorsen's</span>
        <span class="line-sub">Construction L.L.C</span>
      </p>
    </div>
    <ul class="service-list">
      <li>Disaster Recovery</li>
      <li>Storm Damage Restoration</li>
      <li>Proactive Disaster Plan Management</li>
      <li>Roof Repair/Restoration</li>
      <li>Structural Repair and Reconstruction</li>
      <li>Emergency Boarding and Tarping Service</li>
      <li>Perimeter Fencing</li>
      <li>Emergency Tree Removal</li>
    </ul>
    <div class="owners">
      <p class="owner-names">Derek &amp; Milton Halvorsen</p>
      <p class="owner-role">OWNER OPERATORS</p>
      <div class="phone-divider">
        <span class="rule"></span>
        <svg width="30" height="30" viewBox="0 0 30 30" aria-hidden="true">
          <circle cx="15" cy="15" r="15" fill="#1b8fe4"/>
          <path d="M11.2 8.5c.5-.3 1.1-.2 1.4.3l1.5 2.4c.3.5.2 1.1-.2 1.4l-1 .8c.7 1.6 2 2.9 3.6 3.6l.8-1c.3-.4.9-.5 1.4-.2l2.4 1.5c.5.3.6.9.3 1.4l-.9 1.4c-.4.6-1.1.9-1.8.7-4.2-1-7.5-4.3-8.5-8.5-.2-.7.1-1.4.7-1.8z" fill="#ffffff"/>
        </svg>
        <span class="rule"></span>
      </div>
      <p class="phone-number">(541) 823 - 7906</p>
    </div>
  </section>
</body>
</html>
```